Packaging for Hair Fibers Product

We are a start up company looking for a new packaging design for hair building fibers. These are aimed at predominantly men but also women as well. We already have a logo and i have the packaging design from our competitors. We are wanting to keep the look masculine as 90% of our users will be middle aged men. We would like the colours to be black and white but are open to other colours as well.
It will need to have our logo and the following somewhere on the front.
"Instant Fuller & Thicker Hair" & "Natural Hair Building Fibers" "28g" or "Net Weight 28g"
We only need the front of the packaging designed, please make the other sides of the packaging the same colour but blank.
Target Market(s)
Men 25+
Industry/Entity Type
Hair And Beauty
Requirements
Must have
- Logo which i have included. and the following somewhere on the front.
- "Instant Fuller & Thicker Hair" ; "Natural Hair Building Fibers" "28g" or "Net Weight 28g"
Nice to have
- Make it stand out from the competition or similar to the brantiq example.

```html
<!DOCTYPE html>
<html lang="en">
<head>
<meta charset="utf-8">
<title>Manecraft Hair Building Fibers – Front Panel</title>
<link rel="stylesheet" href="https://fonts.googleapis.com/css2?family=Montserrat:wght@300;400;700;800&display=swap">
<style>
  :root {
    --page-bg: #ffffff;
    --panel-black: #0b0b0c;
    --panel-edge: #1a1a1c;
    --frame-grey: #3a3a3d;
    --label-grey-light: #2c2c2f;
    --label-grey-dark: #161618;
    --logo-silver: #e6e6e8;
    --blue-bright: #2a8cf5;
    --blue-light: #3aa0ff;
    --blue-deep: #0c3f8c;
    --band-text: #e9edf3;
  }
  * { box-sizing: border-box; margin: 0; padding: 0; }
  html, body {
    width: 1118px;
    height: 1200px;
    overflow: hidden;
    background: var(--page-bg);
  }
  .canvas {
    position: relative;
    width: 1118px;
    height: 1200px;
  }
  .front-panel {
    position: absolute;
    left: 289px;
    top: 40px;
    width: 540px;
    height: 1120px;
    background: linear-gradient(160deg, #141416 0%, var(--panel-black) 45%, #0e0e10 100%);
    border: 1px solid var(--panel-edge);
    font-family: "Montserrat", sans-serif;
  }
  .logo-frame {
    position: absolute;
    left: 38px;
    top: 84px;
    width: 356px;
    height: 187px;
    border: 2px solid var(--frame-grey);
    border-bottom: none;
    background: #070708;
    display: flex;
    align-items: center;
    justify-content: center;
  }
  .brand-name {
    color: var(--logo-silver);
    font-weight: 300;
    font-size: 46px;
    letter-spacing: 6px;
    text-transform: uppercase;
  }
  .product-label {
    position: absolute;
    left: 38px;
    top: 271px;
    width: 356px;
    height: 375px;
    background: radial-gradient(ellipse at 50% 40%, var(--label-grey-light) 0%, var(--label-grey-dark) 100%);
    text-align: left;
    padding: 52px 0 0 66px;
    color: var(--blue-bright);
  }
  .product-label .scent {
    display: block;
    font-weight: 300;
    font-size: 38px;
    line-height: 1;
    letter-spacing: -0.5px;
    color: var(--blue-light);
  }
  .product-label .word-hair {
    display: block;
    font-weight: 800;
    font-size: 98px;
    line-height: 0.92;
    letter-spacing: -2px;
    margin-top: 2px;
  }
  .product-label .word-building {
    display: block;
    font-weight: 800;
    font-size: 52px;
    line-height: 1;
    letter-spacing: -1px;
  }
  .product-label .word-fibers {
    display: block;
    font-weight: 800;
    font-size: 70px;
    line-height: 0.98;
    letter-spacing: -1.5px;
  }
  .benefit-band {
    position: absolute;
    left: 81px;
    top: 796px;
    width: 270px;
    height: 119px;
    background: linear-gradient(90deg, #0a1c3d 0%, #14468f 55%, #1a55a8 100%);
    display: flex;
    flex-direction: column;
    justify-content: center;
    align-items: center;
    color: var(--band-text);
    text-transform: uppercase;
  }
  .benefit-band .line-one {
    font-weight: 700;
    font-size: 22px;
    letter-spacing: 1.5px;
  }
  .benefit-band .line-two {
    font-weight: 700;
    font-size: 30px;
    letter-spacing: 1.5px;
    margin-top: 6px;
  }
  .net-weight {
    position: absolute;
    left: 0;
    width: 100%;
    top: 1020px;
    text-align: center;
    font-weight: 300;
    font-size: 28px;
    color: var(--blue-bright);
  }
</style>
</head>
<body>
<main class="canvas">
  <section class="front-panel" aria-label="Front of the hair fibers box">
    <div class="logo-frame">
      <span class="brand-name">Manecraft</span>
    </div>
    <div class="product-label">
      <span class="scent">FRAGRANCE</span>
      <span class="word-hair">HAIR</span>
      <span class="word-building">BUILDING</span>
      <span class="word-fibers">FIBERS</span>
    </div>
    <div class="benefit-band">
      <span class="line-one">Instant Fuller &amp;</span>
      <span class="line-two">Thicker Hair</span>
    </div>
    <p class="net-weight">Net Weight 28g</p>
  </section>
</main>
</body>
</html>
```